Saffron Lantern Court Business Card

I am looking for a business card desgined for my restaurant. It is an Indian restaurant, we are looking for something thats modern, yet traditional with the indian culture, we are looking for colors that match our logo. The logo is a design of the building with the name of the restaurant. for more information on the restaurant go to www.saffronlanterncourt.example

Industry/Entity Type

Indian Restaurant

Contact Information for Business Card

we are looking for somthing thats modern, yet traditional with the indian culture, we are looking for colors that match our logo. The logo is a design of the building with the name of the restaurant. for more information on the restaurant go to www.saffronlanterncourt.example

Requirements
Must have
• The logo that is attached,
• Name: Harvinder Oberoi,
• address of the restaurant: 7328 West Larkspur Rd, Phoenix, Arizona, 85213
• Phone: (602) 555-0147
• Fax: (602) 555-0193
• Restaurant Catering Banquet
• Website: www.SaffronLanternCourt.example
Nice to have
• wanted to get something that goes with the theme of the restaurant, which is traditional but also keep a very professional and modern touch

```html
<!DOCTYPE html>
<html lang="en">
<head>
<meta charset="utf-8">
<title>Saffron Lantern Court Business Card</title>
<link href="https://fonts.googleapis.com/css2?family=Federo&family=Montserrat:wght@500&family=Roboto:wght@400&display=swap" rel="stylesheet">
<style>
  :root {
    --backdrop: #e6e6e6;
    --maroon: #8f2723;
    --maroon-deep: #7d1f1c;
    --saffron: #e8731c;
    --paper: #fbfaf8;
    --ink: #7a1e1c;
    --cream: #fdf6ef;
  }
  * { box-sizing: border-box; margin: 0; padding: 0; }
  html, body { width: 1200px; height: 855px; overflow: hidden; background: var(--backdrop); }
  .canvas { position: relative; width: 1200px; height: 855px; }

  .card {
    position: absolute; top: 148px; width: 344px; height: 570px;
    border-radius: 8px; overflow: hidden;
  }
  .card--front { left: 199px; }
  .card--back { left: 629px; background: var(--paper); }

  .damask-field {
    position: absolute; inset: 0;
    background: linear-gradient(180deg, var(--maroon) 0%, var(--maroon-deep) 100%);
  }
  .card--back .damask-field { bottom: auto; height: 293px; }
  .card--back .chevron { position: absolute; left: 0; top: 0; width: 344px; height: 293px; }

  .fringe-band {
    position: absolute; left: 10px; right: 10px; height: 14px;
    background: linear-gradient(180deg, var(--saffron) 0 3px, rgba(232,115,28,0.55) 3px 100%);
  }
  .card--front .fringe-band--top { top: 11px; }
  .card--front .fringe-band--bottom { top: 544px; }
  .card--back .fringe-band--bottom { top: 541px; }

  .brand {
    position: absolute; left: 0; right: 0; text-align: center;
    font-family: "Federo", sans-serif; color: var(--cream);
    text-transform: uppercase; line-height: 1;
  }
  .card--front .brand { top: 222px; font-size: 56px; letter-spacing: 2px; }
  .card--front .brand span { display: block; height: 60px; }
  .card--back .brand { top: 104px; font-size: 40px; letter-spacing: 1px; }
  .card--back .brand span { display: block; height: 42px; }

  .brand-rule { position: absolute; height: 1px; background: var(--saffron); }
  .card--front .brand-rule { left: 82px; width: 180px; top: 400px; }
  .card--back .brand-rule { left: 100px; width: 144px; top: 235px; }

  .since {
    position: absolute; left: 0; right: 0; text-align: center;
    font-family: "Montserrat", sans-serif; font-weight: 500; color: var(--cream);
    letter-spacing: 2.4px;
  }
  .card--front .since { top: 408px; font-size: 11px; }
  .card--back .since { top: 241px; font-size: 8.5px; }

  .holder {
    position: absolute; top: 331px; left: 0; right: 0; text-align: center;
    font-family: "Federo", sans-serif; font-size: 25px; color: var(--ink);
  }
  .contact {
    position: absolute; left: 0; right: 0; text-align: center;
    font-family: "Roboto", sans-serif; font-size: 14.5px; line-height: 19px; color: var(--ink);
  }
  .contact--lines { top: 397px; }
  .contact--address { top: 470px; }
  .label, .accent { color: var(--saffron); }
  .contact-rule { position: absolute; left: 41px; width: 262px; top: 458px; height: 1px; background: var(--saffron); }
</style>
</head>
<body>
<main class="canvas">
  <section class="card card--front" aria-label="Business card front">
    <div class="damask-field" role="img" aria-label="Deep red card face with a faint damask floral pattern"></div>
    <div class="fringe-band fringe-band--top" role="img" aria-label="Saffron tasselled fringe border"></div>
    <h1 class="brand"><span>Saffron</span><span>Lantern</span><span>Court</span></h1>
    <div class="brand-rule"></div>
    <p class="since">Since 1985</p>
    <div class="fringe-band fringe-band--bottom" role="img" aria-label="Saffron tasselled fringe border"></div>
  </section>

  <section class="card card--back" aria-label="Business card back">
    <div class="damask-field" role="img" aria-label="Deep red header with a faint damask floral pattern"></div>
    <svg class="chevron" viewBox="0 0 344 293" aria-hidden="true">
      <polygon points="0,266 172,293 344,266 344,293 0,293" fill="var(--paper)"/>
    </svg>
    <h2 class="brand"><span>Saffron</span><span>Lantern</span><span>Court</span></h2>
    <div class="brand-rule"></div>
    <p class="since">Since 1985</p>

    <p class="holder">Harvinder Oberoi</p>
    <p class="contact contact--lines">
      <span class="label">Ph.:</span> (602) 555-0147<br>
      <span class="label">Fax:</span> (602) 555-0193<br>
      www.<span class="accent">SaffronLanternCourt</span>.example
    </p>
    <div class="contact-rule"></div>
    <p class="contact contact--address">7328 West Larkspur Rd, Phoenix,<br>Arizona, 85213</p>
    <div class="fringe-band fringe-band--bottom" role="img" aria-label="Saffron tasselled fringe border"></div>
  </section>
</main>
</body>
</html>
```